ORVILMA card Technical Architecture

Hello everyone ORVILMA: It is a consulting firm in Architecture and Construction. I require a card duplexing, sober, elegant, classic but not boring. Update 1: Use the following data for the card. Name: Rodrigo Salinas Tomás Quevedo Position: COO Twitter: @orvilmaAT Homepage: orvilma.com home address not include the participation of all thank you.

Target Market(s)

Construction companies, Architects and Consulting Engineers

Industry/Entity Type

Consulting

Contact Information for Business Card

Los campos que debe tener:
Nombre, Cargo, email, homepage y twitter

Font styles to use
Serif
Sans Serif
Other font styles liked:
• Me gustan playfair display, open sans y roboto, pero estoy sujeto a sus propuestas

Requirements
Must have
• Colors: Present combined proposals in white, red, gray and black Update 1: The two names must be clearly differentiated from the two surnames
Nice to have
• They are free to present their best proposals. I will bring them immediate feedback to the extent you can go see their designs. Complete data for card and logo files will give the winner the

```html
<!DOCTYPE html>
<html lang="es">
<head>
<meta charset="utf-8">
<title>ORVILMA — Tarjeta de presentación</title>
<link href="https://fonts.googleapis.com/css2?family=Montserrat:wght@400;500;700&display=swap" rel="stylesheet">
<style>
  :root {
    --stage: #2e2e2e;
    --card-dark: #2a2a2a;
    --card-light: #ffffff;
    --accent-red: #c4161c;
    --deep-red: #6d0a0e;
    --ink: #2b2b2b;
    --muted: #555555;
    --rule: #8a8a8a;
    --strip-grey: #3a3a3a;
  }
  * { margin: 0; padding: 0; box-sizing: border-box; }
  html, body {
    width: 1200px;
    height: 900px;
    overflow: hidden;
    background: var(--stage);
    font-family: "Montserrat", sans-serif;
  }
  .stage {
    width: 1200px;
    height: 900px;
    display: flex;
    flex-direction: column;
    align-items: center;
    justify-content: center;
    gap: 36px;
  }
  .card {
    position: relative;
    width: 700px;
    height: 400px;
    border-radius: 22px;
    overflow: hidden;
    box-shadow: 0 12px 30px rgba(0,0,0,0.45);
  }
  .card-shapes {
    position: absolute;
    inset: 0;
    width: 100%;
    height: 100%;
  }

  /* Back side */
  .card-back { background: var(--card-dark); }
  .back-mark {
    position: absolute;
    top: 120px;
    left: 0;
    width: 100%;
    text-align: center;
    color: var(--card-light);
    font-weight: 700;
    font-size: 52px;
    letter-spacing: 14px;
  }
  .social-handle {
    position: absolute;
    left: 34px;
    bottom: 22px;
    display: flex;
    align-items: center;
    gap: 12px;
    font-size: 17px;
    color: var(--ink);
  }
  .social-dot {
    width: 12px;
    height: 12px;
    border-radius: 50%;
    background: var(--accent-red);
  }

  /* Front side */
  .card-front { background: var(--card-light); }
  .person {
    position: absolute;
    top: 38px;
    right: 40px;
    width: 340px;
    text-align: right;
  }
  .person-line {
    display: flex;
    justify-content: flex-end;
    align-items: baseline;
    gap: 12px;
  }
  .person-given {
    color: var(--deep-red);
    font-weight: 700;
    font-size: 27px;
  }
  .person-family {
    color: var(--deep-red);
    font-weight: 700;
    font-size: 27px;
  }
  .person-role {
    font-size: 14px;
    color: var(--ink);
  }
  .person-rule {
    height: 1px;
    background: var(--rule);
    margin: 6px 0 4px;
  }
  .person-dept {
    font-size: 15px;
    color: var(--ink);
  }
  .brand {
    position: absolute;
    left: 60px;
    top: 175px;
    display: flex;
    align-items: center;
    gap: 14px;
  }
  .brand-square {
    width: 22px;
    height: 22px;
    background: var(--accent-red);
  }
  .brand-name {
    font-weight: 500;
    font-size: 40px;
    letter-spacing: 10px;
    color: var(--ink);
  }
  .contact {
    position: absolute;
    left: 50px;
    bottom: 34px;
    width: 300px;
    border-top: 1px solid var(--rule);
    padding-top: 10px;
    list-style: none;
  }
  .contact-item {
    display: flex;
    align-items: center;
    gap: 12px;
    font-size: 17px;
    color: var(--ink);
    line-height: 1.45;
  }
  .contact-icon {
    width: 12px;
    height: 12px;
    flex: none;
  }
</style>
</head>
<body>
<main class="stage">

  <section class="card card-back" aria-label="Reverso de la tarjeta">
    <svg class="card-shapes" viewBox="0 0 700 400" aria-hidden="true">
      <polygon points="440,322 700,296 700,318 470,344" fill="var(--accent-red)"/>
      <polygon points="0,318 420,318 470,344 700,344 700,400 0,400" fill="var(--card-light)"/>
    </svg>
    <div class="back-mark">ORVILMA</div>
    <p class="social-handle"><span class="social-dot"></span>@orvilmaAT</p>
  </section>

  <section class="card card-front" aria-label="Anverso de la tarjeta">
    <svg class="card-shapes" viewBox="0 0 700 400" aria-hidden="true">
      <polygon points="0,384 590,384 586,400 0,400" fill="var(--strip-grey)"/>
      <polygon points="612,262 700,262 700,400 600,400" fill="var(--strip-grey)"/>
      <polygon points="622,262 700,262 700,400 612,400" fill="var(--deep-red)" transform="translate(0,0)"/>
      <polygon points="600,300 620,262 700,262 700,320 612,384" fill="var(--deep-red)"/>
    </svg>

    <div class="person">
      <div class="person-line">
        <span class="person-given">Rodrigo Salinas</span>
      </div>
      <div class="person-role">COO</div>
      <div class="person-line">
        <span class="person-family">Tomás Quevedo</span>
      </div>
      <div class="person-rule"></div>
      <div class="person-dept">Director de Operaciones</div>
    </div>

    <div class="brand">
      <span class="brand-square"></span>
      <span class="brand-name">ORVILMA</span>
    </div>

    <ul class="contact">
      <li class="contact-item">
        <svg class="contact-icon" viewBox="0 0 12 12" aria-hidden="true"><path d="M2 1l2 0 1 3-1.5 1a6 6 0 0 0 3.5 3.5l1-1.5 3 1v2a1 1 0 0 1-1 1A9 9 0 0 1 1 2a1 1 0 0 1 1-1z" fill="var(--deep-red)"/></svg>
        (+571) 555 010 2040
      </li>
      <li class="contact-item">
        <svg class="contact-icon" viewBox="0 0 12 12" aria-hidden="true"><rect x="1" y="2.5" width="10" height="7" fill="none" stroke="var(--deep-red)" stroke-width="1.4"/><path d="M1 3l5 4 5-4" fill="none" stroke="var(--deep-red)" stroke-width="1.2"/></svg>
        info@orvilma.com
      </li>
      <li class="contact-item">
        <svg class="contact-icon" viewBox="0 0 12 12" aria-hidden="true"><circle cx="6" cy="6" r="5" fill="none" stroke="var(--deep-red)" stroke-width="1.3"/><path d="M1 6h10M6 1c-2.5 3-2.5 7 0 10M6 1c2.5 3 2.5 7 0 10" fill="none" stroke="var(--deep-red)" stroke-width="1"/></svg>
        www.orvilma.com
      </li>
    </ul>
  </section>

</main>
</body>
</html>
```